Clockharbour Homepage Banner 1060 W x 100 H

Please see the attached 'word' document (Also copied below)
Feel free to use any images or logos from our website.
www.clockharbour.com.au

Background:
We are an Australian based official watch distributor/online retailer of international watch brands.

We require a new banner ad (1060 W x 100 H) to replace the existing one on our homepage www.clockharbour.com.au & wish to convey the following information:
*(Please feel free to alter wording, include or exclude points below & generally take creative license (with commercial reality in mind). We sell some luxury watches, so it must look professional & maintain a luxury look & feel.)

Clockharbour Direct:
Revolutionising the retail watch market !

- Buy direct from the official distributor & get world competitive
online prices (with full international warranty, & all original
papers, box & invoice)

- Eliminate all risk of fakes & non-existent factory warranty from
'grey' market sellers

- Free worldwide delivery over A$300

- Order online & 'try-on' in the comfort of your own home.
If you're not 100% happy, just post it back for a full refund or
exchange within 30 days

- Prefer to see & try on before purchase? Visit one of our retail
partner stores.

*** Feel free to copy any images from our website
www.clockharbour.com.au
Updates

Target Market(s)

Luxury watches

Industry/Entity Type

Retail

Font styles to use
Sans Serif

Requirements
Must have
• Visual imagery, text
Nice to have
• Feel free to use your creativity...
Should not have
• Cheap looking or tacky images. We sell some luxury watches, so we need to keep a professional & luxury image.

```html
<!DOCTYPE html>
<html lang="en">
<head>
<meta charset="utf-8">
<title>Clockharbour Homepage Banner</title>
<link rel="stylesheet" href="https://fonts.googleapis.com/css2?family=Archivo+Black&family=Lora:wght@700&display=swap">
<style>
  :root {
    --leather-dark: #5a3413;
    --leather-mid: #8f5523;
    --leather-light: #b87834;
    --watch-steel: #d9d6d0;
    --watch-shadow: #6b4a2c;
    --text-light: #ffffff;
    --text-shadow: rgba(40, 20, 5, 0.55);
  }
  * { margin: 0; padding: 0; box-sizing: border-box; }
  html, body {
    width: 1200px;
    height: 113px;
    overflow: hidden;
    background: var(--leather-dark);
  }
  .banner {
    position: relative;
    width: 1200px;
    height: 113px;
    overflow: hidden;
  }
  .leather-backdrop {
    position: absolute;
    inset: 0;
    background:
      radial-gradient(ellipse at 55% 40%, var(--leather-light) 0%, var(--leather-mid) 55%, var(--leather-dark) 100%);
  }
  .watch-photo {
    position: absolute;
    left: 0;
    top: 0;
    width: 176px;
    height: 113px;
    background:
      radial-gradient(circle at 38% 48%, var(--watch-steel) 0%, var(--watch-steel) 38%, var(--watch-shadow) 62%, transparent 78%);
  }
  .offer {
    position: absolute;
    left: 176px;
    right: 0;
    top: 0;
    height: 113px;
    color: var(--text-light);
    text-align: center;
    text-shadow: 1px 1px 2px var(--text-shadow);
  }
  .offer-headline {
    position: absolute;
    left: 0;
    right: 0;
    top: 24px;
    font-family: "Archivo Black", "Arial Black", sans-serif;
    font-size: 29px;
    line-height: 1;
    font-weight: 400;
    padding-left: 0;
    transform: translateX(-8px);
  }
  .offer-guarantee {
    position: absolute;
    left: 0;
    right: 0;
    top: 64px;
    font-family: "Lora", Georgia, serif;
    font-size: 20.5px;
    line-height: 1.1;
    font-weight: 700;
    white-space: nowrap;
    transform: translateX(8px);
  }
</style>
</head>
<body>
  <div class="banner">
    <div class="leather-backdrop" role="img" aria-label="Brown leather texture background"></div>
    <div class="watch-photo" role="img" aria-label="Photo of a luxury wristwatch with white dial and rose-gold case"></div>
    <div class="offer">
      <p class="offer-headline">FREE WORLDWIDE DELIVERY OVER A$300</p>
      <p class="offer-guarantee">If you're not 100% happy, just post it back for a full refund or exchange within 30 days</p>
    </div>
  </div>
</body>
</html>
```